Lumora Ad Image for "7 Habits of Calm Morning Gardeners"

Please use one of the attached images.

The headline should be, "7 Habits of Calm Morning Gardeners"

I want it to really catch the eye of people as they scroll Lumora :)

```html
<!DOCTYPE html>
<html lang="en">
<head>
<meta charset="utf-8">
<title>7 Habits of Calm Morning Gardeners – Lumora Ad</title>
<link rel="stylesheet" href="https://fonts.googleapis.com/css2?family=Montserrat:wght@800;900&display=swap">
<style>
  :root {
    --page-bg: #ffffff;
    --card-bg: #ffffff;
    --pattern-a: #ffffff;
    --pattern-b: #eef5fc;
    --blue: #1d8fd6;
    --orange: #f8aa1c;
    --ring: #3a9ee0;
    --photo-light: #fbfcfd;
    --photo-mid: #e9eef3;
    --photo-shirt: #3a77b6;
    --photo-deep: #2a5f98;
  }
  * { margin: 0; padding: 0; box-sizing: border-box; }
  html, body {
    width: 1200px;
    height: 1200px;
    overflow: hidden;
    background: var(--page-bg);
    font-family: "Montserrat", sans-serif;
  }
  .ad-card {
    position: absolute;
    left: 87px;
    top: 331px;
    width: 1026px;
    height: 539px;
    background: var(--card-bg);
    box-shadow: 0 1px 4px rgba(0, 0, 0, 0.28);
    overflow: hidden;
  }
  .card-backdrop {
    position: absolute;
    inset: 0;
    width: 100%;
    height: 100%;
  }
  .headline {
    position: absolute;
    inset: 0;
    text-transform: uppercase;
    line-height: 1;
    font-weight: 900;
  }
  .headline > span {
    position: absolute;
    white-space: nowrap;
  }
  .headline-number {
    left: 58px;
    top: 39px;
    font-size: 248px;
    color: var(--orange);
  }
  .headline-small {
    right: 581px;
    top: 207px;
    font-size: 41px;
    font-weight: 800;
    color: var(--blue);
  }
  .headline-calm {
    right: 581px;
    top: 263px;
    font-size: 66px;
    color: var(--blue);
  }
  .headline-morning {
    right: 581px;
    top: 335px;
    font-size: 68px;
    color: var(--orange);
  }
  .headline-tail {
    right: 581px;
    top: 415px;
    font-size: 47px;
    font-weight: 800;
    color: var(--blue);
  }
  .portrait {
    position: absolute;
    left: 527px;
    top: 49px;
    width: 440px;
    height: 440px;
  }
</style>
</head>
<body>
  <section class="ad-card">
    <svg class="card-backdrop" viewBox="0 0 1026 539" preserveAspectRatio="none" role="img" aria-label="Faint pale blue pattern of rising trend arrows across the background">
      <defs>
        <linearGradient id="backdropFill" x1="0" y1="1" x2="1" y2="0">
          <stop offset="0" stop-color="var(--pattern-b)"/>
          <stop offset="0.5" stop-color="var(--pattern-a)"/>
          <stop offset="1" stop-color="var(--pattern-b)"/>
        </linearGradient>
      </defs>
      <rect width="1026" height="539" fill="url(#backdropFill)"/>
    </svg>
    <h1 class="headline">
      <span class="headline-number">7</span>
      <span class="headline-small">Habits of</span>
      <span class="headline-calm">Calm</span>
      <span class="headline-morning">Morning</span>
      <span class="headline-tail">Gardeners</span>
    </h1>
    <svg class="portrait" viewBox="0 0 440 440" role="img" aria-label="Portrait photo of a smiling presenter in a blue Fernhollow Studio t-shirt with arms crossed, on a white backdrop">
      <defs>
        <linearGradient id="portraitFill" x1="0" y1="0" x2="0" y2="1">
          <stop offset="0" stop-color="var(--photo-light)"/>
          <stop offset="0.38" stop-color="var(--photo-mid)"/>
          <stop offset="0.62" stop-color="var(--photo-shirt)"/>
          <stop offset="1" stop-color="var(--photo-deep)"/>
        </linearGradient>
      </defs>
      <circle cx="220" cy="220" r="218" fill="url(#portraitFill)" stroke="var(--ring)" stroke-width="2.5"/>
    </svg>
  </section>
</body>
</html>
```